Space Game inspiration Sketches / Concept Art

We need some fresh design ideas for our Veltapad app interface.
It's a space game where you fly about and visit planets. We'd like a slightly soviet propaganda design style - see the stamp examples for the kind of ideas I mean. Although if you have a fantastic idea feel free to go with it.
Don't worry too much about getting things exact - at the moment we are just looking for concept art rather than a finished product. I have included two screenshots from the dev version of the game to show you an example of the game screens.
EDIT: Some people have mentioned the brief is a little vague - to clarify please submit:
- the two screenshots attached recreated in a 'soviet' style (at least 1334px x 750px 326ppi or larger, RGB colours)
- A color palette and a list of fonts used.
Updates
Project Deadline Extended
Reason: As it's Christmas a few designers have commented they are very busy - I've extended the deadline so you don't have to work over the holiday. :)
Target Market(s)
18-40 yo males
Confident Gamers,
Already play console or PC games
Professionals
High level of education
Industry/Entity Type
Product
Look and feel

```html
<!DOCTYPE html>
<html lang="en">
<head>
<meta charset="utf-8">
<title>Planet Card – Level 3</title>
<link rel="stylesheet" href="https://fonts.googleapis.com/css2?family=Black+Ops+One&family=Comfortaa:wght@500;700&display=swap">
<style>
  :root {
    --backdrop: #1d2126;
    --board: #6b4a2e;
    --board-dark: #4a321e;
    --paper: #e6d6b6;
    --paper-edge: #c9ad7d;
    --ink: #1a1715;
    --muted: #7b746b;
    --alert: #c4141b;
    --metal-light: #d9dad6;
    --metal-dark: #8a8c88;
    --scene-sky: #e89a2a;
    --scene-ground: #a3180f;
    --scene-water: #7e9a4a;
    --tile: #e9e4d6;
  }
  * { margin: 0; padding: 0; box-sizing: border-box; }
  html, body { width: 800px; height: 1200px; overflow: hidden; background: var(--backdrop); }
  .canvas { position: relative; width: 800px; height: 1200px; background: var(--backdrop); }

  .hud-strip { position: absolute; top: 0; left: 0; right: 0; height: 50px; display: flex; justify-content: flex-end; gap: 10px; padding: 12px 20px 0 0; }
  .hud-tile { width: 42px; height: 26px; border-radius: 6px; background: var(--tile); font: 700 12px "Comfortaa", sans-serif; color: var(--ink); display: flex; align-items: center; justify-content: center; }
  .hud-tile.count { background: #fff; }

  .board { position: absolute; left: 4px; top: 36px; width: 792px; height: 1164px; background: linear-gradient(160deg, var(--board), var(--board-dark)); border-radius: 26px 26px 0 0; }
  .paper { position: absolute; left: 18px; top: 56px; width: 764px; height: 1132px; background: radial-gradient(ellipse at center, #efe2c4 40%, var(--paper) 70%, var(--paper-edge) 100%); border-radius: 6px; box-shadow: 0 2px 6px rgba(0,0,0,.4); }

  .clip { position: absolute; left: 200px; top: 0; width: 400px; height: 130px; }

  .level { position: absolute; right: 56px; top: 244px; font: 28px "Black Ops One", sans-serif; letter-spacing: 3px; color: var(--ink); }

  .planet-view { position: absolute; left: 43px; top: 292px; width: 721px; height: 308px; border: 6px solid var(--ink); border-radius: 6px; background: linear-gradient(180deg, #6fa29a 0%, var(--scene-sky) 35%, var(--scene-ground) 62%, var(--scene-water) 78%, var(--scene-ground) 100%); }

  .planet-name { position: absolute; left: 0; right: 0; top: 612px; text-align: center; font: 66px "Black Ops One", sans-serif; letter-spacing: 6px; color: var(--ink); }
  .planet-blurb { position: absolute; left: 50px; right: 50px; top: 712px; text-align: center; font: 500 34px/46px "Comfortaa", sans-serif; color: var(--ink); }

  .actions { position: absolute; left: 0; right: 0; top: 912px; height: 200px; }
  .action { position: absolute; top: 0; width: 200px; height: 200px; }
  .action svg { position: absolute; inset: 0; }
  .action span { position: absolute; inset: 0; display: flex; align-items: center; justify-content: center; font: 24px "Black Ops One", sans-serif; color: var(--muted); }
  .action.attack { left: 69px; }
  .action.upgrade { left: 304px; }
  .action.abandon { left: 542px; }
  .action.abandon span { color: var(--alert); }
</style>
</head>
<body>
<div class="canvas">
  <div class="hud-strip">
    <div class="hud-tile"></div>
    <div class="hud-tile">141</div>
    <div class="hud-tile"></div>
    <div class="hud-tile"></div>
    <div class="hud-tile count">321</div>
  </div>

  <div class="board"></div>
  <div class="paper"></div>

  <svg class="clip" viewBox="0 0 400 130">
    <defs>
      <linearGradient id="metal" x1="0" y1="0" x2="0" y2="1">
        <stop offset="0" stop-color="var(--metal-light)"/>
        <stop offset="1" stop-color="var(--metal-dark)"/>
      </linearGradient>
    </defs>
    <path d="M30 128 L70 60 L330 60 L370 128 Z" fill="url(#metal)" stroke="#5c5e5a" stroke-width="3"/>
    <rect x="110" y="40" width="180" height="28" rx="8" fill="url(#metal)" stroke="#5c5e5a" stroke-width="3"/>
    <path d="M170 42 Q170 4 200 4 Q230 4 230 42" fill="none" stroke="#9ea09b" stroke-width="10"/>
  </svg>

  <div class="level">LEVEL 3</div>

  <div class="planet-view" role="img" aria-label="Poster-style landscape of red mountains around a green lake under an orange sunset sky"></div>

  <h1 class="planet-name">NAMEOS</h1>
  <p class="planet-blurb">Lorem ipsum dolor sit amet, consectetur adipiscing elit. Cras mattis tempus augue, at iaculis enim sodales sed.</p>

  <div class="actions">
    <div class="action attack">
      <svg viewBox="0 0 200 200"><path d="M100 8 L192 100 L100 192 L8 100 Z" fill="none" stroke="var(--muted)" stroke-width="10"/><path d="M100 30 L170 100 L100 170 L30 100 Z" fill="none" stroke="var(--muted)" stroke-width="3"/></svg>
      <span>ATTACK</span>
    </div>
    <div class="action upgrade">
      <svg viewBox="0 0 200 200"><path d="M100 8 L192 100 L100 192 L8 100 Z" fill="none" stroke="var(--muted)" stroke-width="10"/><path d="M100 30 L170 100 L100 170 L30 100 Z" fill="none" stroke="var(--muted)" stroke-width="3"/></svg>
      <span>UPGRADE</span>
    </div>
    <div class="action abandon">
      <svg viewBox="0 0 200 200"><path d="M100 8 L192 100 L100 192 L8 100 Z" fill="none" stroke="var(--alert)" stroke-width="10"/><path d="M100 30 L170 100 L100 170 L30 100 Z" fill="none" stroke="var(--alert)" stroke-width="3"/></svg>
      <span>ABANDON</span>
    </div>
  </div>
</div>
</body>
</html>
```